Labor & Delivery Medical Device Quick Reference Guide

We need a quick reference guide updated for a labor and delivery medical device. The content of the piece is in the old sales sheet.

You can learn about the product here: www.velatracecheck.com

I have uploaded the old design.

I am looking for something bright, attractive, clean. The old design is old and boring.

You do not need to use the colors in the logos that I have attached but the logos do need to be on the document. NIVA Scan is the product and Harbor Medworks is the manufacturer.

Target Market(s)

Nurses on the labor and delivery floor
Lab techs in hospital laboratories
Obstetricians

Industry/Entity Type

Medical Equipment

Colors
ffffff

Requirements
Must have
• Must have the content from the old design. Content meaning all the words and images.
Nice to have
• The content is most important but the design needs to support the content. The design needs to be bright and attractive.

```html
<!DOCTYPE html>
<html lang="en">
<head>
<meta charset="utf-8">
<title>NIVA Scan Inservice Guide</title>
<link rel="stylesheet" href="https://fonts.googleapis.com/css2?family=Open+Sans:wght@400;600;700&display=swap">
<style>
  :root {
    --bg: #e6e6e6;
    --page: #ffffff;
    --row-alt: #f1f1f2;
    --row-line: #dcdde0;
    --ink: #5b6670;
    --ink-soft: #8a949c;
    --green: #8cc63f;
    --navy: #2a5ea8;
    --art: #e3e6ea;
  }
  * { box-sizing: border-box; margin: 0; padding: 0; }
  html, body { width: 1200px; height: 800px; overflow: hidden; }
  body {
    background: var(--bg);
    font-family: "Open Sans", sans-serif;
    color: var(--ink);
    display: flex;
    align-items: center;
    justify-content: center;
  }
  .spread {
    width: 1100px;
    height: 720px;
    display: flex;
    box-shadow: 0 10px 30px rgba(0,0,0,.12);
  }
  .page {
    width: 550px;
    height: 100%;
    background: var(--page);
    display: flex;
    flex-direction: column;
    position: relative;
  }
  .page--left { border-right: 1px solid var(--row-line); }
  .page-header {
    height: 78px;
    display: flex;
    align-items: center;
    justify-content: space-between;
    padding: 0 28px;
  }
  .guide-title {
    font-size: 26px;
    font-weight: 400;
    color: var(--ink);
    letter-spacing: .2px;
  }
  .guide-title strong { color: var(--green); font-weight: 700; }
  .brand {
    display: flex;
    align-items: center;
    gap: 6px;
    font-size: 20px;
    font-weight: 700;
    color: var(--navy);
  }
  .brand-dot { width: 10px; height: 10px; border-radius: 50%; background: var(--navy); }
  .steps { list-style: none; flex: 1; display: flex; flex-direction: column; }
  .step {
    flex: 1;
    display: flex;
    align-items: center;
    gap: 20px;
    padding: 0 28px;
    border-top: 1px solid var(--row-line);
    clip-path: polygon(0 0, 46% 0, 50% 8px, 54% 0, 100% 0, 100% 100%, 0 100%);
  }
  .step:nth-child(odd) { background: var(--row-alt); }
  .step-art {
    flex: none;
    width: 74px;
    height: 56px;
    border-radius: 6px;
    background: var(--art);
  }
  .step-text {
    flex: 1;
    text-align: right;
    font-size: 14px;
    line-height: 1.45;
    color: var(--ink);
  }
  .page-foot {
    padding: 12px 28px 16px;
    display: flex;
    flex-direction: column;
    gap: 8px;
  }
  .foot-brand { align-self: flex-end; }
  .warning { font-size: 11.5px; line-height: 1.45; color: var(--ink); }
  .contact { font-size: 11px; line-height: 1.5; color: var(--ink-soft); text-align: right; }
  .contact .links { color: var(--green); font-weight: 600; font-size: 12px; }
</style>
</head>
<body>
  <main class="spread">
    <section class="page page--left">
      <header class="page-header">
        <h1 class="guide-title">Inservice Guide-<strong>Point of Care</strong></h1>
      </header>
      <ol class="steps">
        <li class="step">
          <div class="step-art" role="img" aria-label="Hands holding the buffer vial upright"></div>
          <p class="step-text">Remove contents from package. Holding the buffer vial in an upright position, remove the shipping cap and set it aside.</p>
        </li>
        <li class="step">
          <div class="step-art" role="img" aria-label="Swab being removed from its pouch to collect a sample"></div>
          <p class="step-text">Remove swab from its sterile pouch and collect a sample from the posterior fornix.</p>
        </li>
        <li class="step">
          <div class="step-art" role="img" aria-label="Swab placed in the buffer vial and broken at the scored mark"></div>
          <p class="step-text">Place the swab in the buffer. Break off the swab at the scored mark and leave the tip in the vial.</p>
        </li>
        <li class="step">
          <div class="step-art" role="img" aria-label="Shipping cap placed back on the vial"></div>
          <p class="step-text">Place the shipping cap back on the vial and return the vial to the lab.</p>
        </li>
      </ol>
      <footer class="page-foot">
        <div class="brand foot-brand"><span class="brand-dot"></span>NIVA Scan</div>
        <p class="warning">Warning: The test may report positive results in patients with intact membranes and therefore decisions to induce labor should not be based solely on the NIVA Scan test results.</p>
      </footer>
    </section>

    <section class="page page--right">
      <header class="page-header">
        <h1 class="guide-title">Inservice Guide-<strong>Lab</strong></h1>
        <div class="brand"><span class="brand-dot"></span>NIVA Scan</div>
      </header>
      <ol class="steps">
        <li class="step">
          <div class="step-art" role="img" aria-label="Hand holding the buffer vial upright"></div>
          <p class="step-text">Holding the buffer vial in an upright position, remove the shipping cap by twisting.</p>
        </li>
        <li class="step">
          <div class="step-art" role="img" aria-label="Shipping cap replaced with dropper cap"></div>
          <p class="step-text">Replace shipping cap with drop dispensing cap.</p>
        </li>
        <li class="step">
          <div class="step-art" role="img" aria-label="Drops placed into the test cassette well"></div>
          <p class="step-text">Place 4 to 6 drops of solution into the well on the test cassette.</p>
        </li>
        <li class="step">
          <div class="step-art" role="img" aria-label="Thumbs pressing the timer on the test cassette"></div>
          <p class="step-text">Place test cassette on a flat surface and start timer by pressing with your thumbs from the bottom of the timer tip.</p>
        </li>
        <li class="step">
          <div class="step-art" role="img" aria-label="Timer and test cassette"></div>
          <p class="step-text">Wait 3 to 5 minutes for test result to interpret.</p>
        </li>
        <li class="step">
          <div class="step-art" role="img" aria-label="Positive, negative and invalid test result examples"></div>
          <p class="step-text">Read the test result.</p>
        </li>
      </ol>
      <footer class="page-foot contact">
        <p class="links">harbormedworks.com | velatracecheck.com</p>
        <p>Harbor Medworks, 1200 Shoreline Way, Bayport, MN 55000 | Toll free 1.800.555.0142</p>
        <p>NIVA Scan is a trademark of Harbor Medworks. All rights reserved. Rev. A</p>
      </footer>
    </section>
  </main>
</body>
</html>
```